Brightmere Business Card Redesign & Logo Update

We need to update our business cards to something more modern and fresh. Brightmere can provide the current color schemes and old design examples, but welcome creativity in helping us with this redesign. PLEASE NOTE that we no longer utilize the "tree" and/or "leaf" imagery in our branding. If able would apprecaite an update on the quality of our "words only" logo in Ai. / PNG formats too.

Target Market(s)

Investors, landowners, corporate partners, contractors

Industry/Entity Type

Environmental Restoration & Conservation

Contact Information for Business Card

Logo, persons name, title, mailing address, phone and email, website url

Font styles to use
Other font styles liked:
• Merriweather

Requirements
Nice to have
• Logo, persons name, title, mailing address, phone and email, website url, but open to ideams
Should not have
• No all back backgrounds

```html
<!DOCTYPE html>
<html lang="en">
<head>
<meta charset="utf-8">
<title>Brightmere Business Card</title>
<link href="https://fonts.googleapis.com/css2?family=Bebas+Neue&family=Arimo:wght@400&display=swap" rel="stylesheet">
<style>
  :root{
    --bg:#e6e6e6;
    --paper:#f7f7f7;
    --orange:#e07a00;
    --orange-deep:#dc7300;
    --green:#1f8a3e;
    --grey:#5a5a5a;
    --rule:#9a9a9a;
    --white:#f8f8f8;
  }
  html,body{margin:0;padding:0;overflow:hidden;}
  body{width:1200px;height:1200px;background:var(--bg);position:relative;}
  .card{position:absolute;left:262px;width:686px;height:392px;border-radius:18px;box-shadow:0 6px 14px rgba(0,0,0,.18);overflow:hidden;}
  .card-front{top:165px;background:var(--paper);}
  .card-back{top:653px;background:linear-gradient(180deg,var(--orange),var(--orange-deep));}
  .brand-name{position:absolute;font-family:"Arimo",sans-serif;font-weight:400;line-height:1;white-space:nowrap;text-align:center;letter-spacing:2px;margin:0;}
  .front-brand{left:60px;width:290px;top:177px;font-size:36px;color:var(--orange);}
  .back-brand{left:0;right:0;top:168px;font-size:62px;color:var(--white);letter-spacing:4px;}
  .divider{position:absolute;left:369px;top:107px;width:1px;height:182px;background:var(--rule);}
  .details{position:absolute;left:393px;top:98px;font-family:"Arimo",sans-serif;color:var(--grey);}
  .person{font-family:"Bebas Neue",sans-serif;font-weight:400;font-size:33px;line-height:1;margin:0;}
  .person .first{color:var(--orange);}
  .person .last{color:var(--green);}
  .role{font-size:15px;margin:2px 0 12px;color:#777;}
  .address{font-size:16px;line-height:21px;margin:0 0 8px;}
  .contacts{list-style:none;margin:0;padding:0;font-size:16px;}
  .contacts li{display:flex;align-items:center;height:20.5px;}
  .contacts svg{width:13px;height:13px;margin:0 12px 0 3px;fill:var(--orange);}
</style>
</head>
<body>
  <section class="card card-front">
    <p class="brand-name front-brand">BRIGHTMERE</p>
    <div class="divider"></div>
    <div class="details">
      <h1 class="person"><span class="first">DANIEL</span> <span class="last">MORGAN</span></h1>
      <p class="role">Managing Director</p>
      <p class="address">4120 Juniper Court<br>Fairbanks, Alaska 99701</p>
      <ul class="contacts">
        <li><svg viewBox="0 0 16 16"><path d="M3 1l3 0 1 4-2 1.5c1 2 2.5 3.5 4.5 4.5L11 9l4 1v3c0 1-1 2-2 2C7 15 1 9 1 3c0-1 1-2 2-2z"/></svg>555-318-2046</li>
        <li><svg viewBox="0 0 16 16"><path d="M4 0h8a1 1 0 0 1 1 1v14a1 1 0 0 1-1 1H4a1 1 0 0 1-1-1V1a1 1 0 0 1 1-1zm1 2v10h6V2zm3 11a1 1 0 1 0 0 2 1 1 0 0 0 0-2z"/></svg>555-792-4180</li>
        <li><svg viewBox="0 0 16 16"><path d="M1 3h14v10H1zm1.5 1.2L8 8.5l5.5-4.3V12h-11z"/></svg>info@brightmere.com</li>
        <li><svg viewBox="0 0 16 16"><circle cx="8" cy="8" r="7"/></svg>www.brightmere.com</li>
      </ul>
    </div>
  </section>
  <section class="card card-back">
    <p class="brand-name back-brand">BRIGHTMERE</p>
  </section>
</body>
</html>
```